Business Card Design

Motorvane Ledger is an online automotive resource on a national scale specifically targeting lease purchases for new cars. Our Online and app platform allow prospective lease clients to scan a window sticker while at a franchise dealership and instantly receive a lease quote at what we call the sweet spot. Motorvane Ledger offers price transparency during the lease process to allow average people the confidence in the lease process and takes away any fear of the big franchise dealers.
Motorvane ledger allows ordinary lease customers to know they are getting a low price lease and not overpaying. Never overpay again

Industry/Entity Type

Automotive

Contact Information for Business Card

Motorvane Ledger
Martin Sowerby (President of operations)
Phone: 888-247-6031
Cell: 561-384-2706

```html
<!DOCTYPE html>
<html lang="en">
<head>
<meta charset="utf-8">
<title>Motorvane Ledger – Business Card</title>
<link href="https://fonts.googleapis.com/css2?family=Montserrat:wght@800&family=Open+Sans:wght@400;600;700&display=swap" rel="stylesheet">
<style>
  :root {
    --backdrop: #4b4b4b;
    --card-dark: #231f20;
    --card-light: #ffffff;
    --ink-light: #ffffff;
    --ink-dark: #1c1a1b;
  }
  html, body {
    margin: 0;
    padding: 0;
    overflow: hidden;
  }
  .canvas {
    position: relative;
    width: 1200px;
    height: 1000px;
    background: var(--backdrop);
    overflow: hidden;
    font-family: "Open Sans", Arial, sans-serif;
  }
  .card {
    position: absolute;
    box-shadow: 0 3px 8px rgba(0,0,0,0.45);
    overflow: hidden;
  }
  /* Back side */
  .card-back {
    left: 155px;
    top: 127px;
    width: 613px;
    height: 360px;
    background: var(--card-dark);
    color: var(--ink-light);
    text-align: center;
  }
  .card-back .brand-name {
    position: absolute;
    left: 0;
    right: 0;
    top: 200px;
    font-family: "Montserrat", Arial, sans-serif;
    font-weight: 800;
    font-size: 44px;
    line-height: 1;
    letter-spacing: 0.5px;
    text-transform: uppercase;
    color: var(--ink-light);
  }
  .card-back .website {
    position: absolute;
    left: 0;
    right: 0;
    top: 273px;
    font-weight: 700;
    font-size: 16px;
  }
  /* Front side */
  .card-front {
    left: 423px;
    top: 543px;
    width: 590px;
    height: 344px;
    background: var(--card-light);
  }
  .card-front .lower-band {
    position: absolute;
    left: 0;
    top: 0;
    width: 590px;
    height: 344px;
  }
  .card-front .lower-band path { fill: var(--card-dark); }
  .brand-lockup {
    position: absolute;
    top: 58px;
    left: 0;
    right: 0;
    display: flex;
    justify-content: center;
    align-items: center;
    gap: 14px;
  }
  .brand-lockup .brand-square {
    width: 34px;
    height: 34px;
    background: var(--ink-dark);
  }
  .brand-lockup .brand-name {
    font-family: "Montserrat", Arial, sans-serif;
    font-weight: 800;
    font-size: 38px;
    line-height: 0.95;
    text-transform: uppercase;
    color: var(--ink-dark);
  }
  .contact {
    position: absolute;
    left: 0;
    right: 0;
    top: 188px;
    text-align: center;
    color: var(--ink-light);
  }
  .contact .person-name {
    margin: 0;
    font-weight: 600;
    font-size: 19px;
    letter-spacing: 0.3px;
    text-transform: uppercase;
  }
  .contact .person-title {
    margin: 2px 0 0;
    font-size: 14px;
  }
  .contact .details {
    margin: 20px 0 0;
    font-size: 14px;
    line-height: 21px;
  }
</style>
</head>
<body>
<div class="canvas">

  <section class="card card-back">
    <div class="brand-name">Motorvane Ledger</div>
    <div class="website">www.motorvaneledger.com</div>
  </section>

  <section class="card card-front">
    <svg class="lower-band" viewBox="0 0 590 344" aria-hidden="true">
      <path d="M0 180 L55 178 L59 146 Q290 190 522 146 L526 178 L590 180 L590 344 L0 344 Z"/>
    </svg>
    <div class="brand-lockup">
      <div class="brand-square"></div>
      <div class="brand-name">Motorvane<br>Ledger</div>
    </div>
    <div class="contact">
      <p class="person-name">Martin Sowerby</p>
      <p class="person-title">President of Operations</p>
      <p class="details">
        Phone: 888-247-6031<br>
        Cell: 561-384-2706<br>
        740 Harbor Crest Rd. Suite 12, Palm Rivera, FL 33410
      </p>
    </div>
  </section>

</div>
</body>
</html>
```